Banner Ad Design Project

We need a 728x90 and a 300x250
1st option
"I have a lead for you. Click here to close the deal."
In large bold letters.
Under this in smaller letters,
"Brindlow. For serious business networkers"
2nd option
"Put that coffee down!"
"Coffee's for closers only."
Close more deals. BRINDLOW LOGO
(this is a quote from Harrowmere Standoff. It is a famous sales movie)
The other option is
"First you get the money" "Then you get the power" in bold letters.
"Brindlow. For serious business networkers" in smaller letters at the bottom.
-Must have our colors
-Must have our logo (Small at the bottom right)
-Watch the video at brindlow () com
Please be creative. If the banner can have multiple images that would be great as well.
This needs to be a serious looking ad that is bold and clean.
Updates
Please be sure to use the phrase, "Put that coffee down! Coffee's for closers only" with the logo and at the bottom the words, Brindlow, for serious business networkers. in one of the designs. This will be our first campaign. I am looking for a very simple design that is bold. Perhaps just a coffee cup with the words and no other graphics.
Target Market(s)
Sales professionals
Industry/Entity Type
Business
Look and feel
Each slider illustrates characteristics of the customer's brand and the style your logo design should communicate.

```html
<!DOCTYPE html>
<html lang="en">
<head>
<meta charset="utf-8">
<title>Brindlow banner ads</title>
<link href="https://fonts.googleapis.com/css2?family=Ubuntu:wght@400;500&display=swap" rel="stylesheet">
<style>
  :root {
    --stage: #121314;
    --brand-blue: #325a97;
    --brand-blue-edge: #24467f;
    --brand-orange: #f39c12;
    --button-orange: #f5a21b;
    --button-edge: #d9860b;
    --button-text: #1f3560;
    --white: #ffffff;
    --logo-navy: #2f4f8a;
    --tagline-grey: #5d6470;
    --avatar-light: #ffb347;
    --avatar-dark: #f08a12;
  }
  * { margin: 0; padding: 0; box-sizing: border-box; }
  html, body { width: 1200px; height: 900px; overflow: hidden; background: var(--stage); }
  body { position: relative; font-family: "Ubuntu", sans-serif; }

  .banner { position: absolute; overflow: hidden; background: var(--white); border: 1.5px solid var(--brand-blue-edge); }
  .banner-backdrop { position: absolute; inset: 0; width: 100%; height: 100%; }
  .banner > :not(.banner-backdrop) { position: absolute; }

  .headline { color: var(--white); font-weight: 400; white-space: nowrap; line-height: 1; }
  .subline { color: var(--white); font-weight: 400; white-space: nowrap; line-height: 1; letter-spacing: 0.5px; }
  .cta {
    display: flex; align-items: center; justify-content: center;
    background: var(--button-orange); border: 1.5px solid var(--button-edge); border-radius: 3px;
    color: var(--button-text); font-weight: 500; font-size: 22px; letter-spacing: 0.3px; white-space: nowrap;
  }
  .avatar {
    border-radius: 50%; border: 3px solid var(--white);
    background: radial-gradient(circle at 50% 40%, var(--avatar-light), var(--avatar-dark));
  }
  .wordmark { color: var(--logo-navy); font-weight: 400; line-height: 1; letter-spacing: -0.5px; }
  .tagline { color: var(--tagline-grey); font-weight: 400; line-height: 1; white-space: nowrap; }

  /* 300x250 rectangle */
  .banner-rectangle { left: 375px; top: 126px; width: 450px; height: 375px; }
  .banner-rectangle .headline { left: 26px; top: 28px; font-size: 39px; }
  .banner-rectangle .subline { left: 27px; top: 88px; font-size: 30px; }
  .banner-rectangle .cta { left: 29px; top: 154px; width: 238px; height: 57px; }
  .banner-rectangle .avatar { left: 304px; top: 169px; width: 62px; height: 62px; }
  .banner-rectangle .wordmark { left: 33px; top: 290px; font-size: 40px; }
  .banner-rectangle .tagline { left: 33px; top: 337px; font-size: 23px; }

  /* 728x90 leaderboard */
  .banner-leaderboard { left: 55px; top: 586px; width: 1090px; height: 135px; }
  .banner-leaderboard .wordmark { left: 16px; top: 24px; font-size: 40px; }
  .banner-leaderboard .tagline { left: 12px; top: 87px; font-size: 22px; }
  .banner-leaderboard .headline { left: 248px; top: 22px; font-size: 39px; }
  .banner-leaderboard .subline { left: 250px; top: 79px; font-size: 30px; }
  .banner-leaderboard .avatar { left: 657px; top: 72px; width: 46px; height: 46px; }
  .banner-leaderboard .cta { left: 834px; top: 39px; width: 234px; height: 56px; }
</style>
</head>
<body>

<section class="banner banner-rectangle" aria-label="Brindlow 300 by 250 banner">
  <svg class="banner-backdrop" viewBox="0 0 450 375" preserveAspectRatio="none" aria-hidden="true">
    <path d="M0 0 H450 V262 Q230 262 0 232 Z" fill="var(--brand-blue)"/>
    <path d="M0 232 Q230 262 450 262 V284 Q240 272 0 238 Z" fill="var(--brand-orange)"/>
  </svg>
  <h1 class="headline">Put that coffee down?</h1>
  <p class="subline">Coffee's for closers only</p>
  <a class="cta">GET BETTER LEADS</a>
  <div class="avatar" role="img" aria-label="Small icon of a sales professional"></div>
  <div class="wordmark">brindlow</div>
  <p class="tagline">Close more deals</p>
</section>

<section class="banner banner-leaderboard" aria-label="Brindlow 728 by 90 banner">
  <svg class="banner-backdrop" viewBox="0 0 1090 135" preserveAspectRatio="none" aria-hidden="true">
    <rect width="1090" height="135" fill="var(--brand-blue)"/>
    <path d="M0 0 H222 Q204 60 196 135 H0 Z" fill="var(--white)"/>
    <path d="M222 0 H240 Q224 60 216 135 H196 Q204 60 222 0 Z" fill="var(--brand-orange)"/>
  </svg>
  <div class="wordmark">brindlow</div>
  <p class="tagline">Close more deals</p>
  <h1 class="headline">Put that coffee down?</h1>
  <p class="subline">Coffee's for closers only</p>
  <div class="avatar" role="img" aria-label="Small icon of a sales professional"></div>
  <a class="cta">GET BETTER LEADS</a>
</section>

</body>
</html>
```